New Branding Business Card Design

Redesign business card according to new branding update.

** The design received so far are single color + BLACK.
I'd encourage designer to use different tones of blue / purple as described in the Designer Brief color palette

Target Market(s)

International

Industry/Entity Type

Medical Equipment

Contact Information for Business Card

Logo on one side (Designer can decide if they want to move certain info from the other side to save space)

Main body info (company name, individual name in both English and Chinese, contact info etc) on the other
Prefer a 'cleaner' layout - vs 'all over the place'
Prefer flush left alignment

Font styles to use
Sans Serif

Requirements
Must have
• Key info
• (Company name (English)): VORAM (HK) Limited
• (Name (English)): Marcus L. Pryde
• (Credential): FCPA, FHKSI
• (Title): Founder, Managing Director & CEO
• For the following info, designers decide whether to use colon or no colon, stroke separator, or use icon gfx for T (for telephone fixed line, M for mobile etc.)
• T: +852 3517 VORAM / +852 3517 4062
• M: +852 6243 7719 / + 86 139 2745 3186
• E: marcus.l.pryde@voram-example.hk
Nice to have
• Depending on the space and spacing available designers can add or use fuller title and other info
• Title: Chairman of the Executive Committee, Founder, Managing Director & CEO
• (Name (Chinese)): 林書恒
Should not have
• One of our business entities a long company name that cannot be broken into 2 lines
• makes vertical implementation almost impossible

```html
<!DOCTYPE html>
<html lang="en">
<head>
<meta charset="utf-8">
<title>VORAM Business Card</title>
<link rel="stylesheet" href="https://fonts.googleapis.com/css2?family=Open+Sans:wght@400;600&family=Noto+Sans+TC:wght@400&display=swap">
<style>
  :root {
    --stage: #202020;
    --card: #1b1b1c;
    --purple: #5e2e8f;
    --purple-light: #7a45b0;
    --silver: #d9d9d9;
    --text: #f2f2f2;
    --rule: #3a3a3c;
  }
  * { margin: 0; padding: 0; box-sizing: border-box; }
  html, body { width: 1200px; height: 900px; overflow: hidden; }
  body {
    background: var(--stage);
    font-family: "Open Sans", sans-serif;
    display: flex;
    flex-direction: column;
    align-items: center;
    justify-content: center;
    gap: 48px;
  }
  .card {
    width: 580px;
    height: 348px;
    background: var(--card);
    border-radius: 24px;
    box-shadow: 0 16px 36px rgba(0,0,0,0.55);
    position: relative;
  }
  .card-front {
    display: flex;
    align-items: center;
    justify-content: center;
  }
  .brand {
    display: flex;
    align-items: center;
    gap: 16px;
    font-weight: 600;
    letter-spacing: 0.08em;
  }
  .brand-square { border-radius: 8px; }
  .card-front .brand { color: var(--silver); font-size: 44px; }
  .card-front .brand-square { width: 44px; height: 44px; background: var(--silver); }

  .card-back {
    display: grid;
    grid-template-columns: 262px 1px 1fr;
    align-items: center;
  }
  .card-back .brand { color: var(--purple); font-size: 36px; justify-self: center; gap: 12px; }
  .card-back .brand-square { width: 34px; height: 34px; background: var(--purple); }
  .divider { width: 1px; height: 232px; background: var(--rule); }
  .details { padding-left: 26px; color: var(--text); }
  .name { color: var(--purple-light); font-weight: 600; font-size: 16px; letter-spacing: 0.02em; }
  .credential { font-size: 12px; }
  .name-zh { color: var(--purple-light); font-family: "Noto Sans TC", sans-serif; font-size: 24px; line-height: 1.2; }
  .title { font-size: 13.5px; line-height: 1.35; margin-bottom: 20px; }
  .contacts { list-style: none; font-size: 14px; line-height: 1.45; }
  .contacts li { display: flex; align-items: center; gap: 9px; }
  .contacts svg { width: 12px; height: 12px; fill: var(--purple-light); flex: none; }
</style>
</head>
<body>
  <section class="card card-front">
    <div class="brand"><span class="brand-square"></span><span>VORAM</span></div>
  </section>

  <section class="card card-back">
    <div class="brand"><span class="brand-square"></span><span>VORAM</span></div>
    <div class="divider"></div>
    <div class="details">
      <p class="name">MARCUS L. PRYDE <span class="credential">FCPA, FHKSI</span></p>
      <p class="name-zh">林書恒</p>
      <p class="title">Founder<br>Managing Director &amp; CEO</p>
      <ul class="contacts">
        <li><svg viewBox="0 0 12 12"><path d="M1 4c0-1.5 2.2-2.5 5-2.5S11 2.5 11 4v1H8.5V4h-5v1H1zM2.5 6h7l1 4.5h-9z"/></svg>+852 3517 VORAM</li>
        <li><svg viewBox="0 0 12 12"><path d="M1 4c0-1.5 2.2-2.5 5-2.5S11 2.5 11 4v1H8.5V4h-5v1H1zM2.5 6h7l1 4.5h-9z"/></svg>+852 3517 4062</li>
        <li><svg viewBox="0 0 12 12"><path d="M3 0.5h6a1 1 0 0 1 1 1v9a1 1 0 0 1-1 1H3a1 1 0 0 1-1-1v-9a1 1 0 0 1 1-1zM3.5 2v7h5V2z"/></svg>+852 6243 7719</li>
        <li><svg viewBox="0 0 12 12"><path d="M3 0.5h6a1 1 0 0 1 1 1v9a1 1 0 0 1-1 1H3a1 1 0 0 1-1-1v-9a1 1 0 0 1 1-1zM3.5 2v7h5V2z"/></svg>+ 86 139 2745 3186</li>
        <li><svg viewBox="0 0 12 12"><path d="M0.5 2.5h11v7h-11zM1.5 3.3v0.6L6 6.8l4.5-2.9v-0.6L6 6z"/></svg>marcus.l.pryde@voram-example.hk</li>
      </ul>
    </div>
  </section>
</body>
</html>
```